Four in One (Flexible infographic for Content Management Industry)

See attachment.
A graphic depicting 4 products, where each can stand on its own and each can be combined with others, but where, if all are taken together, the best result is achieved (the "super product").
Intended use is web. See attached file as an example.
The most basic idea is as the attached diagram shows, where 4 rectangles are arranged in a quadrangle, with a middle rectangle in the center representing the combined 4 products. This concept is fine except it is a bit too obvious as it stands. We are looking for either a variation of this or another concept.
The audience is technical + professional + enterprise - NOT consumers. Hence the design should be conservative in nature.
We are aware of tools like as Canva or Pictogram where such graphics are available, but we are looking for something with a bit more imagination and flexibility.
This graphic should be targeted to web sites and be delivered with vector-based (SVG) graphics.

```html
<!DOCTYPE html>
<html lang="en">
<head>
<meta charset="utf-8">
<title>Four in One – Super Product</title>
<link href="https://fonts.googleapis.com/css2?family=Bebas+Neue&family=Poppins:wght@400;700&display=swap" rel="stylesheet">
<style>
  :root {
    --bg: #2d2d2d;
    --hub-disc: #c4c2c3;
    --ring: #ffffff;
    --orange-deep: #3a2300;
    --ink-dark: #231700;

    --red-tile: #fd4141;
    --red-card: #c02e30;
    --red-edge: #ffb3b3;
    --red-tick: #7be447;

    --cyan-tile: #41fde1;
    --teal-card: #139a8a;
    --cyan-edge: #b9fff3;
    --teal-ink: #0e4b44;
    --teal-tick: #6b2fd9;

    --violet-tile: #7a31fc;
    --violet-card: #5c22c9;
    --violet-edge: #d2b6ff;
    --violet-tick: #3fe2ea;

    --lime-tile: #8ffc43;
    --green-card: #54941f;
    --lime-edge: #dcffc2;
    --green-ink: #1f3a10;
    --green-tick: #e5151c;

    --white: #ffffff;
  }
  * { box-sizing: border-box; margin: 0; padding: 0; }
  html, body { width: 1200px; height: 1200px; overflow: hidden; }
  body { background: var(--bg); position: relative; font-family: "Poppins", sans-serif; }

  .hub-disc {
    position: absolute; left: 405px; top: 405px; width: 388px; height: 388px;
    border-radius: 50%; background: var(--hub-disc);
  }

  .module { position: absolute; width: 522px; height: 271px; border-radius: 31px; }
  .module--docs { left: 71px; top: 264px; background: var(--red-card); }
  .module--security { left: 619px; top: 264px; width: 508px; background: var(--teal-card); }
  .module--erp { left: 71px; top: 650px; width: 525px; height: 273px; background: var(--violet-card); }
  .module--digital { left: 619px; top: 650px; width: 508px; height: 273px; background: var(--green-card); }

  .module__tile {
    position: absolute; left: 0; top: 0; width: 230px; height: 100%;
    border-radius: 31px; border: 2px solid;
  }
  .module--docs .module__tile { background: var(--red-tile); border-color: var(--red-edge); }
  .module--security .module__tile { background: var(--cyan-tile); border-color: var(--cyan-edge); }
  .module--erp .module__tile { background: var(--violet-tile); border-color: var(--violet-edge); }
  .module--digital .module__tile { background: var(--lime-tile); border-color: var(--lime-edge); }

  .module__icon {
    position: absolute; left: 57px; top: 36px; width: 112px; height: 114px; border-radius: 14px;
  }
  .module--docs .module__icon { background: linear-gradient(160deg, #f5d9a8, #f2c230); }
  .module--security .module__icon { background: linear-gradient(160deg, #f8e07a, #4a8fd6); }
  .module--erp .module__icon { background: linear-gradient(160deg, #3cc3ea, #e8e1dc 55%, #f6d10c); }
  .module--digital .module__icon { background: linear-gradient(160deg, #f4a31e, #f9e3b0 55%, #2a6f8a); }

  .module__title {
    position: absolute; left: 0; width: 230px; top: 160px;
    font-family: "Bebas Neue", sans-serif; font-size: 33px; line-height: 31px;
    text-align: center; font-weight: 400;
  }
  .module--docs .module__title { color: var(--white); }
  .module--security .module__title { color: var(--teal-ink); }
  .module--erp .module__title { color: var(--white); top: 163px; }
  .module--digital .module__title { color: var(--green-ink); top: 170px; }

  .module__body { position: absolute; left: 253px; top: 41px; color: var(--white); }
  .module--docs .module__body { width: 252px; }
  .module--security .module__body { width: 200px; top: 43px; }
  .module--erp .module__body { width: 205px; left: 254px; top: 34px; }
  .module--digital .module__body { width: 228px; left: 256px; top: 32px; }

  .module__lede { font-size: 13.4px; line-height: 15.6px; font-weight: 400; }

  .features { list-style: none; margin-top: 17px; display: flex; flex-direction: column; gap: 13px; }
  .module--docs .features { margin-top: 19px; gap: 14px; }
  .module--security .features { margin-top: 17px; gap: 10px; width: 240px; }
  .module--erp .features { margin-top: 21px; gap: 13px; width: 250px; }
  .module--digital .features { margin-top: 18px; gap: 13px; }

  .feature {
    display: flex; align-items: flex-start; gap: 8px;
    font-weight: 700; font-size: 13.2px; line-height: 13.5px;
  }
  .module--security .feature, .module--digital .feature { gap: 13px; }
  .feature svg { flex: 0 0 14px; width: 14px; height: 14px; }
  .module--docs .feature svg { color: var(--red-tick); }
  .module--security .feature svg { color: var(--teal-tick); }
  .module--erp .feature svg { color: var(--violet-tick); }
  .module--digital .feature svg { color: var(--green-tick); }

  .hub {
    position: absolute; left: 485px; top: 485px; width: 228px; height: 228px;
    border-radius: 50%; background: var(--ring);
  }
  .hub__core {
    position: absolute; left: 12px; top: 12px; width: 204px; height: 204px; border-radius: 50%;
    background: radial-gradient(circle at 50% 40%, #f9ab00 0%, #f5a300 62%, #c47f00 80%, var(--orange-deep) 100%);
    box-shadow: inset 0 6px 8px rgba(255,230,150,0.6);
    display: flex; flex-direction: column; align-items: center; justify-content: center;
  }
  .hub__label {
    font-family: "Bebas Neue", sans-serif; font-size: 36px; line-height: 1;
    color: var(--ink-dark); margin-top: -8px;
  }
  .hub__rule { width: 36px; height: 3px; background: var(--white); margin-top: 9px; }
</style>
</head>
<body>

<svg width="0" height="0" style="position:absolute" aria-hidden="true">
  <defs>
    <symbol id="tick" viewBox="0 0 14 14">
      <circle cx="7" cy="7" r="7" fill="currentColor"/>
      <path d="M4 7.2l2 2 4-4.2" fill="none" stroke="#ffffff" stroke-width="1.6" stroke-linecap="round" stroke-linejoin="round"/>
    </symbol>
  </defs>
</svg>

<div class="hub-disc"></div>

<section class="module module--docs">
  <div class="module__tile">
    <div class="module__icon" role="img" aria-label="Icon of a person, a document and a gear linked by arrows"></div>
    <h2 class="module__title">Document<br>Management</h2>
  </div>
  <div class="module__body">
    <p class="module__lede">Streamline document organization, access, and collaboration with easier file storage and sharing, leading to more efficient workflows.</p>
    <ul class="features">
      <li class="feature"><svg><use href="#tick"/></svg>Centralized Document Control</li>
      <li class="feature"><svg><use href="#tick"/></svg>Collaborative Workspace Integration</li>
      <li class="feature"><svg><use href="#tick"/></svg>Automated Compliance</li>
      <li class="feature"><svg><use href="#tick"/></svg>Check 4</li>
    </ul>
  </div>
</section>

<section class="module module--security">
  <div class="module__tile">
    <div class="module__icon" role="img" aria-label="Icon of a folder with a document and a padlock shield"></div>
    <h2 class="module__title">Security and<br>Compliance</h2>
  </div>
  <div class="module__body">
    <p class="module__lede">Benefit from tailored cloud solutions, secure data storage, and expert disaster recovery planning for reliable and scalable IT operations.</p>
    <ul class="features">
      <li class="feature"><svg><use href="#tick"/></svg>Custom Cloud Solutions</li>
      <li class="feature"><svg><use href="#tick"/></svg>Secure Data Storage</li>
      <li class="feature"><svg><use href="#tick"/></svg>Expert Disaster Recovery</li>
      <li class="feature"><svg><use href="#tick"/></svg>Check 4</li>
    </ul>
  </div>
</section>

<section class="module module--erp">
  <div class="module__tile">
    <div class="module__icon" role="img" aria-label="Icon of an ERP chip with a gear and connected nodes"></div>
    <h2 class="module__title">Enterprise<br>Resource Planning</h2>
  </div>
  <div class="module__body">
    <p class="module__lede">Streamline document organization, access, and collaboration with easier file storage and sharing, leading to more efficient workflows.</p>
    <ul class="features">
      <li class="feature"><svg><use href="#tick"/></svg>Integrated Business Processes</li>
      <li class="feature"><svg><use href="#tick"/></svg>Enhanced Decision-Making</li>
      <li class="feature"><svg><use href="#tick"/></svg>Productivity Improvement</li>
      <li class="feature"><svg><use href="#tick"/></svg>Check 4</li>
    </ul>
  </div>
</section>

<section class="module module--digital">
  <div class="module__tile">
    <div class="module__icon" role="img" aria-label="Icon of a laptop showing a code window"></div>
    <h2 class="module__title">Digitital<br>Transformation</h2>
  </div>
  <div class="module__body">
    <p class="module__lede">Turn scanned documents into easily searchable digital archives, boosting efficiency and accessibility.</p>
    <ul class="features">
      <li class="feature"><svg><use href="#tick"/></svg>Instant searchable Archives with OCR</li>
      <li class="feature"><svg><use href="#tick"/></svg>Automated Document Classification</li>
      <li class="feature"><svg><use href="#tick"/></svg>Quillmere and Cloud Blob Ready</li>
      <li class="feature"><svg><use href="#tick"/></svg>Check 4</li>
    </ul>
  </div>
</section>

<div class="hub">
  <div class="hub__core">
    <span class="hub__label">Super Product</span>
    <span class="hub__rule"></span>
  </div>
</div>

</body>
</html>
```